Business Card Design Project - KLB

I am looking for a more sophisticated card design for my company,
"The Kestrel Bureau"

We are a consultancy focused on strategy and change in Associations and professional organisations.

I am a lawyer and psychologist with a PhD and so am looking for something that communicates seriousness and credibility but also quirky creative solutions for strategic problems, which is my field of speciality.

I am looking for something that is quietly spoken, rather than loud colours ('credible' and 'creative' are the two adjectives that I think of as competing here).

I particularly like an embossed card style - heavy white card with plain white or white and black or white and grey text.

The key logo image for the company is a question mark and I am open to suggestions and ideas on design.

I have attached a file that includes a couple of styles that have caught my eye and my thoughts on them. Hopefully they communicate what I'm looking for.
Updates

Thank you for all the great suggestions and designs.

I really appreciated the effort and creative energy you put into your designs. I have now closed the project after selecting a design and advising the successful designer of the card that I am happy with.

Regards

Target Market(s)

Organisations (CEO's and Boards), Governments, Legal professionals, Membership Associations and aspiring professionals.

Industry/Entity Type

Lawyer

Requirements
Must have
• The key logo element is a question mark (?) and this needs to be incorporated.

Embossed style - cut outs or other design ideas interest me too.

The attached file has a number of sample ideas and comments on each one that I like.
Should not have
• I like crisp, modern fonts (Myriads etc...) and do not like embellished fonts or Times etc...

```html
<!DOCTYPE html>
<html lang="en">
<head>
<meta charset="utf-8">
<title>The Kestrel Bureau – Business Card Concepts</title>
<link rel="stylesheet" href="https://fonts.googleapis.com/css2?family=Source+Sans+3:wght@400;600;700&family=Arimo&display=swap">
<style>
  :root {
    --page: #ffffff;
    --ivory: #f8f6e8;
    --ivory-deep: #f1ecda;
    --ivory-edge: #e6dfc8;
    --emboss: #e9e2c8;
    --ink: #3b3b3b;
    --black: #1a1819;
    --gloss: #2c2a2b;
    --accent: #d0101e;
    --label: #111111;
    --leader-red: #e0303a;
  }
  * { margin: 0; padding: 0; box-sizing: border-box; }
  html, body { width: 1200px; height: 848px; overflow: hidden; background: var(--page); }
  .sheet { position: relative; width: 1200px; height: 848px; font-family: "Source Sans 3", sans-serif; }

  .card { position: absolute; width: 498px; height: 277px; background: var(--ivory); overflow: hidden; box-shadow: 0 0 0 1px #efeadb; }
  .card--tl { left: 73px; top: 52px; }
  .card--tr { left: 621px; top: 52px; }
  .card--bl { left: 73px; top: 414px; }
  .card--br { left: 621px; top: 414px; }

  .card__panel { position: absolute; inset: 0; }
  .card__black { position: absolute; left: 0; top: 0; width: 248px; height: 277px; background: var(--black); }

  .details { position: absolute; left: 294px; top: 34px; color: var(--ink); }
  .details__name { font-size: 20px; font-weight: 400; line-height: 1.1; }
  .details__role { font-size: 15.5px; margin-top: 4px; }
  .details__company { font-size: 13px; color: var(--accent); margin-top: 52px; }
  .details__line { font-size: 13px; line-height: 18px; }

  .mark { position: absolute; font-weight: 700; letter-spacing: 2px; line-height: 1; display: flex; align-items: center; gap: 10px; }
  .mark__square { display: block; width: 22px; height: 22px; background: currentColor; }
  .mark--emboss { left: 40px; top: 92px; font-size: 84px; color: var(--emboss); }
  .mark--dark { left: 34px; top: 92px; font-size: 84px; color: var(--gloss); }
  .mark--new { left: 0; right: 0; top: 88px; justify-content: center; font-size: 120px; color: var(--black); }

  .label { position: absolute; font-family: "Arimo", sans-serif; font-size: 18px; color: var(--label); white-space: nowrap; }
  .label--vertical { transform: rotate(-90deg); transform-origin: left top; }

  .leaders { position: absolute; inset: 0; pointer-events: none; }
  .pointer { position: absolute; left: 772px; top: 717px; width: 196px; height: 72px; }
  .pointer__text { position: absolute; left: 0; right: 0; top: 38px; text-align: center; font-family: "Arimo", sans-serif; font-size: 18px; color: #fff; }
</style>
</head>
<body>
<main class="sheet">

  <section class="card card--tl" aria-label="Embossed ivory card">
    <div class="mark mark--emboss">KLB<span class="mark__square"></span></div>
    <div class="details">
      <p class="details__name">Dr. Mara Ellison</p>
      <p class="details__role">Director</p>
      <p class="details__company">The Kestrel Bureau</p>
      <p class="details__line">M.: +61400 283 716</p>
      <p class="details__line">P.: &nbsp;+612 9540 6271</p>
      <p class="details__line">E.: &nbsp;mara@kestrelbureau.com.au</p>
      <p class="details__line">PO: P.O. Box 4418, Linden Vale,</p>
      <p class="details__line">Sydney, Australia</p>
    </div>
  </section>

  <section class="card card--tr" aria-label="Embossed ivory card with stepped panel">
    <svg class="card__panel" width="498" height="277" viewBox="0 0 498 277">
      <polygon points="252,0 252,21 222,21 222,70 194,70 194,180 165,180 165,277 498,277 498,0"
               fill="var(--ivory-deep)" stroke="var(--ivory-edge)" stroke-width="2"/>
    </svg>
    <div class="mark mark--emboss">KLB<span class="mark__square"></span></div>
    <div class="details">
      <p class="details__name">Dr. Mara Ellison</p>
      <p class="details__role">Director</p>
      <p class="details__company">The Kestrel Bureau</p>
      <p class="details__line">M.: +61400 283 716</p>
      <p class="details__line">P.: &nbsp;+612 9540 6271</p>
      <p class="details__line">E.: &nbsp;mara@kestrelbureau.com.au</p>
      <p class="details__line">PO: P.O. Box 4418, Linden Vale,</p>
      <p class="details__line">Sydney, Australia</p>
    </div>
  </section>

  <section class="card card--bl" aria-label="Ivory card with black matte panel">
    <div class="card__black"></div>
    <div class="mark mark--dark">KLB<span class="mark__square"></span></div>
    <div class="details">
      <p class="details__name">Dr. Mara Ellison</p>
      <p class="details__role">Director</p>
      <p class="details__company">The Kestrel Bureau</p>
      <p class="details__line">M.: +61400 283 716</p>
      <p class="details__line">P.: &nbsp;+612 9540 6271</p>
      <p class="details__line">E.: &nbsp;mara@kestrelbureau.com.au</p>
      <p class="details__line">PO: P.O. Box 4418, Linden Vale,</p>
      <p class="details__line">Sydney, Australia</p>
    </div>
  </section>

  <section class="card card--br" aria-label="Logo card">
    <div class="mark mark--new">KLB<span class="mark__square"></span></div>
  </section>

  <svg class="leaders" width="1200" height="848" viewBox="0 0 1200 848">
    <g fill="none" stroke="#222" stroke-width="1">
      <polyline points="73,387 348,387 260,218"/>
      <polyline points="621,387 897,387 809,217"/>
      <line x1="897" y1="387" x2="940" y2="311"/>
    </g>
    <g fill="none" stroke="var(--leader-red)" stroke-width="1">
      <polyline points="73,735 254,735 217,666"/>
      <polyline points="73,788 316,788 226,609"/>
    </g>
  </svg>

  <p class="label" style="left:76px; top:358px;">embossing with inner bevel</p>
  <p class="label" style="left:624px; top:358px;">embossing with inner bevel</p>
  <p class="label" style="left:76px; top:706px;">black matte paint</p>
  <p class="label" style="left:76px; top:759px;">glossy varnish</p>
  <p class="label label--vertical" style="left:590px; top:282px;">matte ivory paper</p>
  <p class="label label--vertical" style="left:590px; top:644px;">matte ivory paper</p>

  <div class="pointer">
    <svg width="196" height="72" viewBox="0 0 196 72"><polygon points="98,0 196,72 0,72" fill="var(--black)"/></svg>
    <p class="pointer__text">new logo</p>
  </div>

</main>
</body>
</html>
```